One of a kind, 100% Pure & Natural Skincare line needs stunning product label

We need product label design for new natural skincare company called Milo & Tess Skincare. We create luxurious, 100% pure & natural skincare that is free from ingredients that may be potentially irritating to the skin. No toxins, preservatives or additives. Our initial product is Harbor Glow Balm, a nourishing face cream that suits discerning women with mature skin and those with dry/sensitive skin needing extra hydration. Also those that choose to minimize their exposure to environmental toxins. Our brand is simple yet elegant, supporting a holistic, authentic lifestyle and embracing natural skincare.

Target Market(s)

Discerning women with mature skin and those with dry/sensitive skin needing extra hydration. Also those that choose to minimize their exposure to environmental toxins.

Industry/Entity Type

Skin Care Product

Font styles to use
Sans Serif
Script

Colors
f9d9e8
fef1ee

Requirements
Must have
• The Logo.
HARBOR GLOW BALM
EMBRACING NATURAL SKINCARE
Labels must be feminine, simple/minimal yet stylish. Uncluttered yet elegant.
This is a very natural product with minimal ingredients.
Nice to have
• The logo can be incorporated in to the label, or It can be left separate as a sticker on top of the jar. The product is a firm balm consistency and is in frosted glass jars with matt silver lids.
Jar height is 45mm, width is 60mm.
Label height: 28mm and length 185mm
Should not have
• Natural or farmers market type theme. No Bold/loud lettering.

```html
<!DOCTYPE html>
<html lang="en">
<head>
<meta charset="utf-8">
<title>Harbor Glow Balm – Label</title>
<link href="https://fonts.googleapis.com/css2?family=Arimo:wght@400;700&display=swap" rel="stylesheet">
<style>
  :root {
    --label-white: #ffffff;
    --label-blush: #fef1ee;
    --label-pink: #f7d7e6;
    --text-grey: #3f3f3f;
    --accent-orchid: #d98bc2;
  }
  html, body {
    margin: 0;
    padding: 0;
    width: 1200px;
    height: 1002px;
    overflow: hidden;
  }
  .label {
    position: relative;
    width: 1200px;
    height: 1002px;
    background: linear-gradient(to bottom,
      var(--label-white) 0px,
      var(--label-white) 110px,
      var(--label-blush) 300px,
      var(--label-pink) 560px,
      var(--label-pink) 1002px);
    font-family: "Arimo", Arial, sans-serif;
    color: var(--text-grey);
    font-size: 25.5px;
    line-height: 31px;
    letter-spacing: -0.4px;
  }
  .brand-header {
    position: absolute;
    left: 0;
    top: 62px;
    width: 1200px;
    text-align: center;
  }
  .brand-name {
    margin: 0;
    font-size: 36px;
    line-height: 42px;
    font-weight: 400;
    letter-spacing: 1px;
    color: var(--text-grey);
  }
  .product-name {
    margin: 22px 0 0;
    font-size: 26px;
    line-height: 30px;
    font-weight: 400;
    letter-spacing: 6px;
    color: var(--text-grey);
  }
  .tagline {
    margin: 12px 0 0;
    font-size: 15px;
    line-height: 20px;
    letter-spacing: 4px;
    color: var(--accent-orchid);
  }
  .text-block {
    position: absolute;
    margin: 0;
    text-align: center;
  }
  .text-block strong { font-weight: 700; }
  .caution { left: 20px; width: 570px; top: 311px; }
  .storage { left: 20px; width: 570px; top: 512px; }
  .ingredients { left: 658px; width: 530px; top: 311px; }
  .directions { left: 658px; width: 530px; top: 451px; }
  .purity-note {
    position: absolute;
    left: 616px;
    top: 303px;
    writing-mode: vertical-rl;
    color: var(--accent-orchid);
    font-size: 25px;
    letter-spacing: 0;
    line-height: 30px;
  }
  .net-contents {
    position: absolute;
    left: 216px;
    top: 668px;
    display: flex;
    align-items: center;
    gap: 42px;
  }
  .pao-icon { width: 34px; height: 42px; }
</style>
</head>
<body>
<main class="label">
  <header class="brand-header">
    <p class="brand-name">Milo &amp; Tess Skincare</p>
    <h1 class="product-name">HARBOR GLOW BALM</h1>
    <p class="tagline">EMBRACING NATURAL SKINCARE</p>
  </header>
  <p class="text-block caution">
    <strong>Caution</strong>: Keep out of reach of children.<br>
    If pregnant or breastfeeding,<br>
    consult your healthcare practitioner.<br>
    Avoid contact with eyes &amp; sensitive areas.<br>
    Allergy patch test recommended.<br>
    If irritation occurs, discontinue use.
  </p>
  <p class="text-block storage">
    Store below 25°C<br>
    MADE IN AUSTRALIA<br>
    B#<br>
    info@milotessskincare.com.au
  </p>
  <div class="net-contents">
    <svg class="pao-icon" viewBox="0 0 34 42" aria-label="Period after opening: 8 months">
      <path d="M7 4 L22 1 L23 6 L8 9 Z" fill="none" stroke="#555" stroke-width="1.5"/>
      <rect x="4" y="14" width="24" height="24" rx="2" fill="none" stroke="#555" stroke-width="1.5"/>
      <line x1="4" y1="18" x2="28" y2="18" stroke="#555" stroke-width="1"/>
      <text x="16" y="32" font-family="Arimo, Arial, sans-serif" font-size="8" text-anchor="middle" fill="#555">8M</text>
    </svg>
    <span class="volume">50ml</span>
  </div>
  <div class="purity-note">This product is pure &amp; natural</div>
  <p class="text-block ingredients">
    Ingredients: tallow from pasture raised<br>
    goats, frankincense, sandalwood &amp;<br>
    myrrh essential oils.
  </p>
  <p class="text-block directions">
    <strong>Directions</strong>: Soften small amount in<br>
    palm of hand &amp; gently massage into<br>
    skin as often as required.
  </p>
</main>
</body>
</html>
```